International Trading Company, 'TAVIK' needs a Business Card

The company name is "TAVIK" and it has own logo design.
I'd like to use its logo on this business card.
I need two side Business Card.
I'll look forward to your great design.
Thank you very much in advance.

Contact Information for Business Card

Company Name : Vola Harbor Limited
Information Example
Tobias Wrenfold
Mobile(use icon please) : 1 (555) 014-2290
Tel(use icon please) : 1 (555) 014-6835
Email(use icon please) : tobias27@volaharbor.example
Address(use icon please) : 482 Larkmoor Rd, New York, NY 10199, USA

```html
<!DOCTYPE html>
<html lang="en">
<head>
<meta charset="utf-8">
<title>TAVIK Business Card</title>
<link href="https://fonts.googleapis.com/css2?family=Lato:wght@400;700;900&display=swap" rel="stylesheet">
<style>
  :root {
    --page: #e7e5e1;
    --ink: #0d0d0d;
    --paper: #ffffff;
    --logo-grey: #5b5b5b;
    --text: #1a1a1a;
  }
  * { margin: 0; padding: 0; box-sizing: border-box; }
  html, body {
    width: 1189px; height: 1200px; overflow: hidden;
    background: var(--page);
    font-family: "Lato", Arial, sans-serif;
  }
  .card {
    position: absolute;
    left: 169px;
    width: 851px;
    height: 487px;
    background: var(--ink);
    overflow: hidden;
    box-shadow: 0 5px 14px rgba(0,0,0,0.25);
  }
  .card--front { top: 111px; }
  .card--back { top: 641px; }

  .brand-name {
    position: absolute;
    font-family: "Lato", Arial, sans-serif;
    font-weight: 900;
    letter-spacing: 10px;
    line-height: 1;
    white-space: nowrap;
  }
  .card--front .brand-name {
    color: var(--logo-grey);
    font-size: 124px;
    left: 220px;
    top: 179px;
  }
  .card--back .brand-name {
    color: var(--ink);
    font-size: 110px;
    left: 432px;
    top: 68px;
  }

  .swoosh { position: absolute; inset: 0; width: 100%; height: 100%; }

  .contact {
    position: absolute;
    left: 43px;
    top: 210px;
    color: var(--text);
  }
  .contact__name {
    font-size: 27px;
    font-weight: 700;
    line-height: 1.1;
  }
  .contact__role {
    font-size: 21px;
    font-weight: 400;
  }
  .contact__address {
    margin-top: 8px;
    font-size: 21px;
    line-height: 28.5px;
  }
  .contact__lines {
    margin-top: 16px;
    list-style: none;
    font-size: 21px;
    line-height: 28.5px;
  }
  .contact__lines li { display: flex; align-items: center; gap: 7px; }
  .contact__lines svg { width: 18px; height: 18px; flex: none; }
</style>
</head>
<body>
  <section class="card card--front">
    <div class="brand-name">TAVIK</div>
  </section>

  <section class="card card--back">
    <svg class="swoosh" viewBox="0 0 851 487" preserveAspectRatio="none" aria-hidden="true">
      <path fill="#ffffff" d="M0,192 C220,60 520,10 851,18 L851,294 C680,420 360,472 0,470 Z"/>
    </svg>
    <div class="brand-name">TAVIK</div>

    <div class="contact">
      <p class="contact__name">Tobias Wrenfold <span class="contact__role">| President</span></p>
      <p class="contact__address">482 Larkmoor Rd<br>New York, NY 10199<br>USA</p>
      <ul class="contact__lines">
        <li>
          <svg viewBox="0 0 20 20" aria-label="Mobile"><rect x="5" y="1.5" width="10" height="17" rx="2" fill="none" stroke="#1a1a1a" stroke-width="1.8"/><circle cx="10" cy="15.5" r="1" fill="#1a1a1a"/></svg>
          1 (555) 014-2290
        </li>
        <li>
          <svg viewBox="0 0 20 20" aria-label="Telephone"><path fill="#1a1a1a" d="M2 7c0-2 3.5-3.5 8-3.5S18 5 18 7v1.5h-4V7H6v1.5H2z"/><path fill="#1a1a1a" d="M5 10h10l2 7H3z"/><circle cx="10" cy="13" r="1.8" fill="#fff"/></svg>
          1 (555) 014-6835
        </li>
        <li>
          <svg viewBox="0 0 20 20" aria-label="Email"><rect x="1.5" y="4" width="17" height="12" fill="none" stroke="#1a1a1a" stroke-width="1.8"/><path d="M1.5 4l8.5 7 8.5-7M1.5 16l6-6M18.5 16l-6-6" fill="none" stroke="#1a1a1a" stroke-width="1.6"/></svg>
          tobias27@tavikharbor.example
        </li>
      </ul>
    </div>
  </section>
</body>
</html>
```